Flyer-Design für Onlineshop für italienische Naturkosmetik
Zielgruppe
Onlineshop für italienische Naturkosmetik aus der Toskana (https://www.lavendo-seifenhaus.com), Zielgruppe Frauen 30+ mit Interesse vegane Lebensweise, Reiseland Italien und naturverbunden
Aufgabenstellung
Benötigt wird ein Paketbeileger beidseitig bedruckt, mit Gutschein wahlweise im Format DIN lang plus (10,5 x 21 cm) oder DIN lang (9,8 x 21 cm). Passende Texte können von der Webseite übernommen werden, zB. Startseite unten.
Die Beileger werden über Versender italienischer Feinkost verteilt. Insofern sind die Empfänger genauso italophil, wie es unsere Zielgruppe auch ist. Naturkosmetik setzen wir gleich mit handmade, kleinen familiengeführten Manufakturen, besten Rohstoffen aus der Region (Olivenöl, Kräuter, Duftöle)
Emotionale Bildsprache, klare Auslobung des Angebots, vertrauensbildende Vorteile (Zertifikate, Bewertungen, Awards). Einige Produkte im Shop wurden 2015 bereits mit dem Glanzfeder Beauty Award ausgezeichnet.

```html
<!DOCTYPE html>
<html lang="de">
<head>
<meta charset="utf-8">
<title>Lavendo Seifenhaus – Paketbeileger</title>
<link href="https://fonts.googleapis.com/css2?family=Source+Sans+3:ital,wght@0,400;0,600;0,700;1,600;1,700&display=swap" rel="stylesheet">
<style>
  :root{
    --stage:#4a4748;
    --cream:#fdf1e7;
    --white:#ffffff;
    --green-brand:#6aaa2a;
    --green-dark:#1d5a3b;
    --orange-top:#f49c21;
    --orange-bottom:#ea760b;
    --text-body:#1d4a33;
  }
  *{box-sizing:border-box;margin:0;padding:0}
  html,body{width:1200px;height:1200px;overflow:hidden;background:var(--stage);font-family:"Source Sans 3",sans-serif}
  .flyer{position:absolute;width:489px;height:977px;background:var(--white);overflow:hidden;box-shadow:0 4px 10px rgba(0,0,0,.45)}
  .flyer--front{left:79px;top:102px}
  .flyer--back{left:644px;top:104px}
  .hero{position:absolute;left:0;top:0;width:489px;height:560px}
  .logo-disc{position:absolute;left:57px;top:-179px;width:374px;height:374px;border-radius:50%;background:var(--cream);box-shadow:0 3px 8px rgba(0,0,0,.35);}
  .logo{position:absolute;left:0;top:220px;width:374px;display:flex;align-items:center;justify-content:center;gap:12px;color:var(--green-brand);font-weight:600}
  .logo-dot{width:46px;height:46px;border-radius:50%;background:var(--green-brand)}
  .logo-name{line-height:1}
  .logo-name span{display:block}
  .logo-name .l1{font-size:50px;letter-spacing:.5px}
  .logo-name .l2{font-size:29px;margin-top:2px}
  .portrait-ring{position:absolute;left:87px;top:413px;width:314px;height:314px;border-radius:50%;background:var(--cream);box-shadow:0 2px 6px rgba(0,0,0,.25)}
  .portrait{position:absolute;left:16px;top:16px;width:282px;height:282px;border-radius:50%;background:radial-gradient(circle at 55% 45%,#f0cbb0 0%,#d98a4f 40%,#8fb552 75%,#5f8f2c 100%)}
  .tagline{position:absolute;left:0;top:736px;width:489px;text-align:center;color:var(--green-dark);font-size:19.5px;line-height:25.5px;text-transform:uppercase}
  .voucher{position:absolute;left:0;top:836px;width:489px;height:141px;background:linear-gradient(var(--orange-top),var(--orange-bottom))}
  .voucher-perf{position:absolute;left:0;top:0;width:489px;height:4px;background:repeating-linear-gradient(90deg,var(--white) 0 5px,transparent 5px 9px)}
  .voucher-frame{position:absolute;left:16px;top:23px;width:437px;height:102px;border:1.5px solid var(--white);outline:1px solid rgba(255,255,255,.8);outline-offset:-5px}
  .voucher-art{position:absolute;right:0;top:0;width:170px;height:141px;background:linear-gradient(135deg,rgba(255,255,255,0) 20%,rgba(255,255,255,.28) 60%,rgba(255,255,255,.1) 100%)}
  .voucher-title{position:absolute;left:43px;top:28px;color:var(--white);font-weight:700;font-style:italic;font-size:35px;letter-spacing:.5px;line-height:1}
  .voucher-note{position:absolute;left:38px;top:68px;color:var(--white);font-weight:600;font-style:italic;font-size:15.5px}
  .voucher-url{position:absolute;left:42px;top:93px;color:var(--white);font-weight:700;font-size:19px}
  .intro-head{position:absolute;left:0;top:351px;width:489px;display:flex;align-items:center;justify-content:center;gap:10px}
  .branch{width:100px;height:44px;background:linear-gradient(90deg,rgba(29,90,59,.05),rgba(29,90,59,.35),rgba(29,90,59,.05));border-radius:50%}
  .intro-title{color:var(--green-dark);font-weight:700;font-size:20px;white-space:nowrap}
  .intro-body{position:absolute;left:59px;top:394px;width:375px;color:var(--text-body);font-size:14.3px;line-height:18px;text-align:justify;hyphens:auto}
  .intro-body p+p{margin-top:18px}
  .badges{position:absolute;left:0;top:750px;width:489px;height:80px}
  .badge{position:absolute}
  .badge--igp{left:22px;top:8px;width:82px;height:62px;border-radius:50%;background:radial-gradient(#e7c53a,#5d8a2e);border:2px solid #3c6d27}
  .badge--geo{left:141px;top:4px;width:72px;height:72px;border-radius:50%;background:radial-gradient(#2a4fa3 55%,#f2c516 57%)}
  .badge--natural{left:254px;top:9px;width:59px;height:59px;border-radius:50%;border:5px solid #6b6b6b;background:var(--white)}
  .badge--rating{left:344px;top:20px;width:38px;height:38px;border-radius:50%;background:radial-gradient(#f4b520 50%,#2f8ed6 52%)}
  .rating{position:absolute;left:386px;top:20px;width:90px;text-align:center}
  .stars{display:block;margin:0 auto}
  .rating-score{display:block;font-size:9px;font-style:italic;font-weight:600;color:#333;margin-top:2px;border-bottom:1px solid #ccc;padding-bottom:1px}
  .rating-count{display:block;font-size:7px;color:#555;margin-top:2px}
</style>
</head>
<body>

<!-- Vorderseite -->
<section class="flyer flyer--front">
  <svg class="hero" viewBox="0 0 489 560" role="img" aria-label="Foto: toskanische Hügellandschaft mit Zypressen, Landhaus und Weinbergen">
    <defs>
      <linearGradient id="landscape" x1="0" y1="0" x2="0" y2="1">
        <stop offset="0" stop-color="#e9d3c4"/>
        <stop offset=".3" stop-color="#d4c07a"/>
        <stop offset=".55" stop-color="#a8b53a"/>
        <stop offset="1" stop-color="#3f7a3a"/>
      </linearGradient>
    </defs>
    <path d="M0 0H489V517Q250 600 0 544Z" fill="url(#landscape)"/>
  </svg>
  <div class="logo-disc">
    <div class="logo"><span class="logo-dot"></span><span class="logo-name"><span class="l1">Lavendo</span><span class="l2">Seifenhaus</span></span></div>
  </div>
  <div class="portrait-ring">
    <div class="portrait" role="img" aria-label="Foto: lächelnde Frau mit roten Locken im Grünen"></div>
  </div>
  <p class="tagline">Natürlich schön. Naturkosmetik berührt<br>unsere Körper und unsere Seele.<br>Jeden Tag!</p>
  <div class="voucher">
    <div class="voucher-perf"></div>
    <div class="voucher-art" role="img" aria-label="Illustration: Olivenzweig in Weiß"></div>
    <div class="voucher-frame"></div>
    <div class="voucher-title">GUTSCHEIN 10 €</div>
    <div class="voucher-note">* gültig bei ihrer ersten Bestellung unter</div>
    <div class="voucher-url">www.lavendo-seifenhaus.com</div>
  </div>
</section>

<!-- Rückseite -->
<section class="flyer flyer--back">
  <svg class="hero" viewBox="0 0 489 560" role="img" aria-label="Foto: grüne Oliven am Zweig vor blauem Himmel">
    <defs>
      <linearGradient id="olives" x1="0" y1="0" x2="1" y2="1">
        <stop offset="0" stop-color="#9fc0e4"/>
        <stop offset=".45" stop-color="#b9c79a"/>
        <stop offset="1" stop-color="#6f9a3c"/>
      </linearGradient>
    </defs>
    <path d="M0 0H489V264Q250 395 0 264Z" fill="url(#olives)"/>
  </svg>
  <div class="logo-disc">
    <div class="logo"><span class="logo-dot"></span><span class="logo-name"><span class="l1">Lavendo</span><span class="l2">Seifenhaus</span></span></div>
  </div>
  <div class="intro-head">
    <span class="branch" role="img" aria-label="Ornament: Olivenzweig"></span>
    <h2 class="intro-title">Von der Natur inspiriert</h2>
    <span class="branch" role="img" aria-label="Ornament: Olivenzweig"></span>
  </div>
  <div class="intro-body">
    <p>Naturkosmetik für Körper, Geist und Seele. Alle für Sie ausgewählte Produkte werden mit großer Leidenschaft und viel Liebe zur Natur entwickelt und hergestellt. Sie beinhalten erlesene Ingredienzien und ausgewählte Pflanzenextrakte. Bei der Herstellung werden natürliche Ressourcen respektiert und Natur, sowie Umwelt geschont.</p>
    <p>Hier finden Sie ein großes, liebevoll zusammengestelltes Sortiment italienischer Naturkosmetik traditioneller Erzeuger aus der Toskana. Ständig auf der Suche nach neuen wohltuenden Schätzen entdecken wir auf provinziellen Wochenmärkten und in kleinen Familienbetrieben immer neue toskanische Pflegekreationen. Wir überzeugen uns vor Ort von der Qualität der Waren und machen uns persönlich ein Bild von der Herstellung und der Philosophie der Erzeuger, um die wir unser Sortiment bereichern. Mit jedem Bad und jeder Pflegeanwendung möchten wir Ihnen Italien und insbesondere die Toskana ein Stückchen näher bringen.</p>
  </div>
  <div class="badges">
    <span class="badge badge--igp" role="img" aria-label="Siegel Olivenöl-Herkunft"></span>
    <span class="badge badge--geo" role="img" aria-label="Siegel geschützte geografische Angabe"></span>
    <span class="badge badge--natural" role="img" aria-label="Siegel zertifizierte Naturkosmetik"></span>
    <span class="badge badge--rating" role="img" aria-label="Siegel Kundenbewertungen"></span>
    <div class="rating">
      <svg class="stars" width="88" height="16" viewBox="0 0 88 16" aria-hidden="true">
        <g fill="#f6c41c">
          <polygon id="star" points="8,0 10,5.6 16,5.8 11.2,9.4 13,15.2 8,11.8 3,15.2 4.8,9.4 0,5.8 6,5.6"/>
          <use href="#star" x="18"/><use href="#star" x="36"/><use href="#star" x="54"/><use href="#star" x="72"/>
        </g>
      </svg>
      <span class="rating-score">4.86 von 5</span>
      <span class="rating-count">aus 234 Bewertungen</span>
    </div>
  </div>
  <div class="voucher">
    <div class="voucher-perf"></div>
    <div class="voucher-art" role="img" aria-label="Illustration: Olivenzweig in Weiß"></div>
    <div class="voucher-frame"></div>
    <div class="voucher-title">GUTSCHEIN 10 €</div>
    <div class="voucher-note">* gültig bei ihrer ersten Bestellung unter</div>
    <div class="voucher-url">www.lavendo-seifenhaus.com</div>
  </div>
</section>

</body>
</html>
```